K&R Security Services PTY. LTD.

Ive just had my logo made and I'm looking for some simple but strong designs for my business cards the company is a security company.

Please use dark colors.

Regards,

Owen Deloit

Reason: Need more time for discussion with other directors

Industry/Entity Type

Security

Font styles to use
Sans Serif
Decorative

```html
<!DOCTYPE html>
<html lang="en">
<head>
<meta charset="utf-8">
<title>K&amp;R Security Services – Business Card</title>
<link rel="stylesheet" href="https://fonts.googleapis.com/css2?family=Open+Sans:wght@400;600;700&family=PT+Serif&family=Marcellus&display=swap">
<style>
  :root {
    --backdrop: #e9e6df;
    --card-orange: #f2a81d;
    --card-yellow: #fcd41c;
    --card-edge: #c98a10;
    --ink-dark: #3a3a3c;
    --ink-grey: #6f6a5e;
    --accent-blue: #3d9ad6;
    --title-white: #fffdf4;
  }
  * { margin: 0; padding: 0; box-sizing: border-box; }
  html, body {
    width: 1200px; height: 800px; overflow: hidden;
    background: var(--backdrop);
  }
  .canvas {
    position: relative; width: 1200px; height: 800px;
    display: flex; flex-direction: column; align-items: center; justify-content: center; gap: 44px;
  }
  .card {
    position: relative; width: 600px; height: 342px;
    border-radius: 3px;
    background: linear-gradient(45deg, var(--card-yellow) 0%, #f8c21c 45%, var(--card-orange) 100%);
    box-shadow: 0 3px 0 var(--card-edge), 0 14px 28px rgba(0,0,0,0.18);
    overflow: hidden;
  }
  .brand {
    display: flex; align-items: center; gap: 12px;
    font-family: "Open Sans", sans-serif; font-weight: 700;
    color: var(--ink-dark); text-transform: uppercase; letter-spacing: 0.04em;
  }
  .brand-mark {
    border-radius: 50%; background: var(--ink-dark); flex: none;
  }
  .card-front .brand {
    position: absolute; left: 50%; top: 50%; transform: translate(-50%, -50%);
    font-size: 30px; white-space: nowrap;
  }
  .card-front .brand-mark { width: 34px; height: 34px; }

  .card-back .brand {
    position: absolute; left: 44px; top: 58px; font-size: 19px;
  }
  .card-back .brand-mark { width: 22px; height: 22px; }

  .holder { position: absolute; left: 78px; top: 204px; }
  .holder-name {
    font-family: "Marcellus", serif; font-size: 22px; letter-spacing: 0.14em;
    color: var(--accent-blue); text-transform: uppercase;
  }
  .holder-title {
    margin-top: 2px; margin-left: 16px;
    font-family: "PT Serif", serif; font-size: 15px; letter-spacing: 0.06em;
    color: var(--title-white);
  }

  .contact {
    position: absolute; left: 340px; top: 104px;
    font-family: "Open Sans", sans-serif; font-size: 12.5px; color: var(--ink-grey);
    list-style: none;
  }
  .contact-row { display: flex; gap: 12px; margin-bottom: 9px; line-height: 1.35; }
  .contact-icon { width: 16px; height: 16px; flex: none; margin-top: 2px; fill: var(--accent-blue); }
  .contact-label { font-size: 10px; display: block; }
</style>
</head>
<body>
<main class="canvas">
  <section class="card card-front" aria-label="Business card front">
    <div class="brand"><span class="brand-mark"></span>K&amp;R Security</div>
  </section>

  <section class="card card-back" aria-label="Business card back">
    <div class="brand"><span class="brand-mark"></span>K&amp;R Security</div>

    <div class="holder">
      <p class="holder-name">Owen Deloit</p>
      <p class="holder-title">Director and Chairman</p>
    </div>

    <ul class="contact">
      <li class="contact-row">
        <svg class="contact-icon" viewBox="0 0 24 24" aria-hidden="true"><path d="M6.6 10.8a15.1 15.1 0 0 0 6.6 6.6l2.2-2.2c.3-.3.7-.4 1-.2 1.1.4 2.3.6 3.6.6.6 0 1 .4 1 1V20c0 .6-.4 1-1 1A17 17 0 0 1 3 4c0-.6.4-1 1-1h3.5c.6 0 1 .4 1 1 0 1.3.2 2.5.6 3.6.1.3 0 .7-.2 1z"/></svg>
        <span>(Home) - (03) 95550418<br>(Mobile) - 0491570263</span>
      </li>
      <li class="contact-row">
        <svg class="contact-icon" viewBox="0 0 24 24" aria-hidden="true"><path d="M12 2a7 7 0 0 0-7 7c0 5.2 7 13 7 13s7-7.8 7-13a7 7 0 0 0-7-7zm0 9.5A2.5 2.5 0 1 1 12 6.5a2.5 2.5 0 0 1 0 5z"/></svg>
        <span><span class="contact-label">Head Office:</span>P.O. Box 7 Elmridge Victoria 3188</span>
      </li>
      <li class="contact-row">
        <svg class="contact-icon" viewBox="0 0 24 24" aria-hidden="true"><path d="M3 5h18v14H3zm2 2v.5l7 4.5 7-4.5V7zm0 2.9V17h14V9.9l-7 4.5z"/></svg>
        <span>owen@krsecure.net.au</span>
      </li>
      <li class="contact-row">
        <svg class="contact-icon" viewBox="0 0 24 24" aria-hidden="true"><path d="M12 2a10 10 0 1 0 0 20 10 10 0 0 0 0-20zm6.9 9h-3a15 15 0 0 0-1.3-5.6A8 8 0 0 1 18.9 11zM12 4.1c.9 1.3 1.7 3.9 1.9 6.9h-3.8c.2-3 1-5.6 1.9-6.9zM9.4 5.4A15 15 0 0 0 8.1 11h-3a8 8 0 0 1 4.3-5.6zM5.1 13h3a15 15 0 0 0 1.3 5.6A8 8 0 0 1 5.1 13zm6.9 6.9c-.9-1.3-1.7-3.9-1.9-6.9h3.8c-.2 3-1 5.6-1.9 6.9zm2.6-1.3a15 15 0 0 0 1.3-5.6h3a8 8 0 0 1-4.3 5.6z"/></svg>
        <span>K.R@krsecure.net.au</span>
      </li>
    </ul>
  </section>
</main>
</body>
</html>
```